Website Required for Small Cyber Security Company

Require a website for Cyber Security company. I have logo which i will attach. Please use logo blue and white as a guide
Would ultimately like the site to have a technology theme with the following pages Landing page
Services
Contact
Careers

I can provide content for each of those pages in due course, until then happy for you to use dummy data to display purposes

Target Market(s)

Government

Industry/Entity Type

Cyber Security

Coding

Coded - Design and coding required

Number of Pages Required

4 page

Colors
0054AA
0677BA
7BADD7
CADEEF
E8F1F8

Requirements
Must have
• High quality finish and UX
Nice to have
• look and feel professional and not cheap

```html
<!DOCTYPE html>
<html lang="en">
<head>
<meta charset="utf-8">
<title>Harbor Ridge Consulting</title>
<link href="https://fonts.googleapis.com/css2?family=Nunito+Sans:wght@400;600;700&display=swap" rel="stylesheet">
<style>
:root{
  --navy:#17213b;
  --blue:#0f7caa;
  --sky:#3898c0;
  --paper:#f0f1f2;
  --stage:#e4e7ec;
  --muted:#5b6275;
}
*{box-sizing:border-box;margin:0;padding:0}
html,body{width:729px;height:1200px;overflow:hidden;background:var(--stage);font-family:"Nunito Sans",sans-serif}
.site{position:absolute;left:67px;top:0;width:941px;height:1898px;background:var(--navy);transform:scale(.6322);transform-origin:0 0;overflow:hidden;color:#fff}
.abs{position:absolute}
.navbar{left:76px;top:14px;width:789px;height:47px;background:var(--paper);border-radius:3px;display:flex;align-items:center;padding-left:14px}
.brand{display:flex;align-items:center;gap:8px;font-weight:700;font-size:14px;color:var(--navy);letter-spacing:.2px}
.brand-dot{width:22px;height:22px;border-radius:50%;background:var(--blue)}
.nav-links{position:absolute;left:482px;top:0;height:47px;display:flex;align-items:center;gap:0}
.nav-links span{font-size:9.5px;color:var(--navy);width:66px;text-align:center}
.nav-cta{position:absolute;right:3px;top:3px;width:42px;height:41px;background:var(--blue);display:flex;align-items:center;justify-content:center}
.hero-photo{left:110px;top:61px;width:430px;height:420px;background:radial-gradient(ellipse at 45% 40%,#3a5bb0 0%,#2a4288 35%,#1d2d5c 65%,rgba(23,33,59,0) 100%)}
.eyebrow{left:547px;top:156px;font-size:9px;letter-spacing:4.6px;color:var(--blue);text-transform:uppercase}
.hero-title{left:547px;top:170px;font-size:40px;line-height:42px;font-weight:600;width:380px}
.accent{color:var(--blue)}
.hero-text{left:552px;top:313px;width:305px;font-size:10.5px;line-height:17px;color:#e2e6ee}
.card{top:462px;width:146px;height:226px;background:var(--paper);color:var(--navy);clip-path:polygon(0 16px,100% 0,100% 211px,0 226px);padding:32px 13px 0}
.card.featured{background:var(--blue);color:#fff}
.card svg{width:28px;height:28px;display:block;margin-bottom:12px}
.card h3{font-size:12px;line-height:16px;font-weight:600;margin-bottom:12px}
.card p{font-size:9.5px;line-height:15.3px;color:var(--muted);padding-left:1px}
.card.featured p{color:#e8f1f8}
.spinner{left:50px;top:662px}
.circuit{left:620px;top:680px;width:321px;height:420px;background:radial-gradient(ellipse at 70% 45%,rgba(56,152,192,.22) 0%,rgba(56,152,192,.08) 45%,rgba(23,33,59,0) 75%)}
.about-title{left:240px;top:758px;width:470px;text-align:center;font-size:32px;line-height:34px;font-weight:600}
.about-text{left:300px;top:890px;width:345px;text-align:center;font-size:10.5px;line-height:16.5px;color:#e2e6ee}
.btn{display:flex;align-items:center;justify-content:center;font-size:8.5px;font-weight:700;letter-spacing:.2px;border-radius:2px}
.btn-light{left:421px;top:966px;width:98px;height:37px;background:#fff;color:var(--blue)}
.careers-panel{left:76px;top:1078px;width:789px;height:576px;background:var(--paper);clip-path:polygon(0 77px,100% 0,100% 492px,0 576px)}
.careers-photo{left:501px;top:1140px;width:307px;height:412px;background:linear-gradient(160deg,#2c48a0 0%,#22377a 45%,#16224a 100%);clip-path:polygon(0 30px,100% 0,100% 378px,0 412px)}
.careers-title{left:152px;top:1250px;font-size:32px;line-height:33px;font-weight:600;color:var(--navy)}
.careers-text{left:152px;top:1336px;width:270px;font-size:10.5px;line-height:16.5px;color:var(--muted)}
.careers-text p+p{margin-top:13px}
.btn-dark{left:152px;top:1477px;width:98px;height:36px;background:var(--blue);color:#fff}
.footer-glow{left:0;top:1690px;width:190px;height:200px;background:radial-gradient(circle at 50% 55%,rgba(56,152,192,.16) 0%,rgba(56,152,192,.05) 50%,rgba(23,33,59,0) 72%)}
.footer-brand{left:76px;top:1760px;color:#fff}
.footer-brand .brand{color:#fff}
.footer-col{top:1726px}
.footer-col h4{font-size:11px;font-weight:600;color:var(--sky);margin-bottom:12px}
.footer-col li{list-style:none;font-size:8.5px;line-height:19.5px;color:#e2e6ee}
.social{display:flex;gap:8px;margin-top:2px}
.social span{width:9px;height:9px;border-radius:50%;background:#fff}
</style>
</head>
<body>
<div class="site">
  <header class="navbar abs">
    <div class="brand"><span class="brand-dot"></span>Harbor Ridge Consulting</div>
    <nav class="nav-links"><span>Home</span><span>About</span><span>Services</span><span>Careers</span></nav>
    <div class="nav-cta">
      <svg width="18" height="14" viewBox="0 0 18 14" fill="none" stroke="#fff" stroke-width="1.4"><rect x="1" y="1" width="16" height="12" rx="1"/><path d="M1 2l8 6 8-6"/></svg>
    </div>
  </header>

  <div class="hero-photo abs" role="img" aria-label="Two IT consultants walking through a server room, one holding a tablet, tinted blue"></div>
  <div class="eyebrow abs">Welcome to Harbor Ridge Consulting</div>
  <h1 class="hero-title abs">Your Go-To for Protecting Your <span class="accent">Online</span> Presence</h1>
  <p class="hero-text abs">From robust firewall solutions that protect your network from external threats to cutting-edge intrusion detection systems that monitor for suspicious activity, we've got you covered.</p>

  <article class="card abs" style="left:76px">
    <svg viewBox="0 0 28 28" fill="none" stroke="#0f7caa" stroke-width="1.2"><circle cx="14" cy="7" r="3.5"/><path d="M8 18c0-4 3-6 6-6s6 2 6 6"/><rect x="7" y="17" width="14" height="7"/><path d="M4 24h20"/></svg>
    <h3>IT support &amp; Managed Services</h3>
    <p>Managed by our expert team, we provide secure, scalable &amp; flexible IT environments demanded by businesses today.</p>
  </article>
  <article class="card abs" style="left:236px">
    <svg viewBox="0 0 28 28" fill="none" stroke="#0f7caa" stroke-width="1.2"><circle cx="14" cy="14" r="11"/><ellipse cx="14" cy="14" rx="5" ry="11"/><path d="M3 14h22M5 8h18M5 20h18"/></svg>
    <h3>Network Penetration Consulting</h3>
    <p>Network penetration testing involves the simulating cyberattacks to test the strength of your defenses.</p>
  </article>
  <article class="card featured abs" style="left:397px">
    <svg viewBox="0 0 28 28" fill="none" stroke="#fff" stroke-width="1.2"><rect x="5" y="4" width="15" height="20" rx="1"/><rect x="9" y="2" width="7" height="4"/><path d="M8 11h9M8 15h9M8 19h5"/><path d="M20 16l5 9h-10z"/></svg>
    <h3>Risk Assessment Services</h3>
    <p>Evaluates potential security risks and helps you prioritize threats, so you can allocate resources effectively.</p>
  </article>
  <article class="card abs" style="left:558px">
    <svg viewBox="0 0 28 28" fill="none" stroke="#0f7caa" stroke-width="1.2"><path d="M14 2l10 4v7c0 6-4 10-10 13C8 23 4 19 4 13V6z"/><rect x="10" y="13" width="8" height="6"/><path d="M11.5 13v-2a2.5 2.5 0 015 0v2"/></svg>
    <h3>Security Awareness and Advisory</h3>
    <p>Our advisory services provide expert guidance to enhance your organization's defenses</p>
  </article>
  <article class="card abs" style="left:719px">
    <svg viewBox="0 0 34 28" fill="none" stroke="#0f7caa" stroke-width="1.2"><rect x="2" y="3" width="30" height="19"/><path d="M0 25h34"/><circle cx="16" cy="11" r="5"/><path d="M20 15l4 4"/></svg>
    <h3>Vulnerability Scans &amp; Cyber Security</h3>
    <p>Vulnerability scans detect weaknesses in your systems and fortify your digital infrastructure against threats.</p>
  </article>

  <svg class="spinner abs" width="50" height="50" viewBox="0 0 50 50" fill="none"><path d="M8 12A22 22 0 0 0 38 44" stroke="#3898c0" stroke-width="2"/></svg>

  <div class="circuit abs" role="img" aria-label="Faint blue circuit board lines with binary digits"></div>
  <h2 class="about-title abs">Empowering <span class="accent">Australian</span> Enterprises since the Early 2000s</h2>
  <p class="about-text abs">At Harbor Ridge Consulting, we specialize in delivering cutting-edge cybersecurity services tailored to the unique needs of government agencies. And not only that.</p>
  <div class="btn btn-light abs">LEARN MORE</div>

  <section class="careers-panel abs"></section>
  <div class="careers-photo abs" role="img" aria-label="Consultant shaking hands with a colleague in a server room, tinted blue"></div>
  <h2 class="careers-title abs">Be a <span class="accent">Part</span> of Us -<br>Explore Careers</h2>
  <div class="careers-text abs">
    <p>With open arms and warm hearts, we wholeheartedly extend our gracious welcome to you, embracing your presence with joy and enthusiasm.</p>
    <p>With open arms and warm hearts, we wholeheartedly extend our gracious welcome to you, embracing your presence with joy and enthusiasm.</p>
  </div>
  <div class="btn btn-dark abs">APPLY TODAY</div>

  <div class="footer-glow abs" role="img" aria-label="Faint blue shield glow"></div>
  <div class="footer-brand abs"><div class="brand"><span class="brand-dot"></span>Harbor Ridge Consulting</div></div>
  <div class="footer-col abs" style="left:519px"><h4>Sitemap</h4><ul><li>Home</li><li>About Us</li><li>Services</li><li>Careers</li></ul></div>
  <div class="footer-col abs" style="left:634px"><h4>Contact Information</h4><ul><li>info@harborridgeconsulting.com</li><li>+1 555 010 2020</li></ul></div>
  <div class="footer-col abs" style="left:811px"><h4>Follow Us</h4><div class="social"><span></span><span></span></div></div>
</div>
</body>
</html>
```